App to track miniature golf scores and provides clues to puzzles (Mabel of Glimmerdeep)

A mini-golf scorecard, selfies, badges, rules and clues. See attached for details. The coding and deployment will be provided by someone else, but those requirements are also listed in doc. We need to be able to update any text fields after design is handed over. This app is only for ios.

Target Market(s)

Families

Industry/Entity Type

Entertainment

Requirements
Must have
• The pages listed in the document is needed. Colors are also provided.
Nice to have
• Small animation effects
Should not have
• dark or psychedelic

```html
<!DOCTYPE html>
<html lang="en">
<head>
<meta charset="utf-8">
<title>Badges</title>
<link href="https://fonts.googleapis.com/css2?family=Open+Sans:wght@400;600;700;800&display=swap" rel="stylesheet">
<style>
  :root {
    --bg-top: #fcdca8;
    --bg-mid: #f9b3a0;
    --bg-bottom: #f587a6;
    --white: #ffffff;
    --ink-dark: #111111;
    --accent: #e9799b;
    --accent-shadow: #d9738f;
    --track: rgba(255, 255, 255, 0.85);
    --ghost: rgba(255, 255, 255, 0.07);
  }
  * { box-sizing: border-box; margin: 0; padding: 0; }
  html, body { width: 675px; height: 1200px; overflow: hidden; }
  body { font-family: "Open Sans", Arial, sans-serif; }

  .screen {
    position: relative;
    width: 675px;
    height: 1200px;
    overflow: hidden;
    background: linear-gradient(180deg, var(--bg-top) 0%, var(--bg-mid) 50%, var(--bg-bottom) 100%);
  }

  .backdrop-art {
    position: absolute;
    left: 110px;
    top: 330px;
    width: 510px;
    height: 510px;
    border-radius: 50%;
    background: var(--ghost);
  }
  .backdrop-title {
    position: absolute;
    left: 0; right: 0;
    top: 70px;
    text-align: center;
    font-weight: 800;
    font-size: 92px;
    letter-spacing: 2px;
    color: rgba(240, 170, 120, 0.12);
  }

  .status-bar {
    position: absolute;
    left: 0; right: 0; top: 0;
    height: 46px;
    display: flex;
    align-items: center;
    justify-content: space-between;
    padding: 0 16px 0 20px;
    color: var(--ink-dark);
    font-size: 20px;
    font-weight: 600;
  }
  .status-left, .status-right { display: flex; align-items: center; gap: 8px; }

  .page-title {
    position: absolute;
    left: 0; right: 0;
    top: 94px;
    text-align: center;
    font-size: 40px;
    font-weight: 700;
    color: var(--white);
    letter-spacing: 0.5px;
  }

  .badge-track {
    position: absolute;
    left: 82px;
    top: 230px;
    width: 11px;
    height: 732px;
    background: var(--track);
  }

  .badge-list { list-style: none; }
  .badge {
    position: absolute;
    left: 37px;
    width: 630px;
    height: 100px;
    display: flex;
    align-items: center;
  }
  .badge-medal {
    flex: none;
    width: 100px;
    height: 100px;
    border-radius: 50%;
    background: var(--white);
    box-shadow: 0 6px 14px rgba(180, 90, 90, 0.25);
    display: flex;
    align-items: center;
    justify-content: center;
  }
  .badge-art {
    width: 52px;
    height: 52px;
    border-radius: 50%;
  }
  .art-bunny { background: radial-gradient(circle, #f2eef4 30%, #d9d1e2 100%); }
  .art-hat { background: radial-gradient(circle, #3a3a3a 40%, #e88a95 100%); }
  .art-cat { background: radial-gradient(circle, #c04fb0 35%, #5fb0c8 100%); }
  .art-mushroom { background: radial-gradient(circle, #8a5a44 40%, #7cb24a 100%); }
  .art-cards { background: radial-gradient(circle, #f4f4f4 35%, #d23a3a 100%); }
  .art-tart { background: radial-gradient(circle, #e9b96a 40%, #d26a6a 100%); }

  .badge-text {
    margin-left: 43px;
    font-size: 22px;
    line-height: 29px;
    color: var(--white);
    font-weight: 400;
    white-space: nowrap;
  }

  .nav-actions {
    position: absolute;
    left: 44px;
    right: 38px;
    top: 1071px;
    display: flex;
    justify-content: space-between;
  }
  .nav-button {
    width: 285px;
    height: 79px;
    border: none;
    border-radius: 8px;
    background: var(--white);
    border-top: 4px solid var(--accent-shadow);
    box-shadow: 0 4px 0 rgba(210, 100, 130, 0.45);
    color: var(--accent);
    font-family: "Open Sans", Arial, sans-serif;
    font-size: 17px;
    font-weight: 700;
    letter-spacing: 0.5px;
  }
</style>
</head>
<body>
<main class="screen">
  <div class="backdrop-art" role="img" aria-label="Faint decorative round background shape"></div>
  <div class="backdrop-title" aria-hidden="true">BADGES</div>

  <header class="status-bar">
    <div class="status-left">
      <svg width="66" height="14" viewBox="0 0 66 14" aria-hidden="true">
        <circle cx="6" cy="7" r="5.5" fill="#111"/>
        <circle cx="19" cy="7" r="5.5" fill="#111"/>
        <circle cx="32" cy="7" r="5.5" fill="#111"/>
        <circle cx="45" cy="7" r="5.5" fill="#111"/>
        <circle cx="58" cy="7" r="5" fill="none" stroke="#111" stroke-width="1.2"/>
      </svg>
      <span>Carrier</span>
      <svg width="20" height="16" viewBox="0 0 20 16" aria-hidden="true">
        <path d="M1 5a13 13 0 0 1 18 0" fill="none" stroke="#111" stroke-width="2.4"/>
        <path d="M4.5 8.5a8 8 0 0 1 11 0" fill="none" stroke="#111" stroke-width="2.4"/>
        <path d="M10 15l-3-3a4 4 0 0 1 6 0z" fill="#111"/>
      </svg>
    </div>
    <div class="status-right">
      <svg width="20" height="20" viewBox="0 0 20 20" aria-hidden="true">
        <circle cx="10" cy="10" r="8" fill="none" stroke="#111" stroke-width="1.8"/>
        <rect x="6.5" y="9" width="7" height="5" fill="#111"/>
        <path d="M8 9V7.5a2 2 0 0 1 4 0V9" fill="none" stroke="#111" stroke-width="1.5"/>
      </svg>
      <span>100%</span>
      <svg width="42" height="18" viewBox="0 0 42 18" aria-hidden="true">
        <rect x="1" y="1" width="36" height="16" rx="3" fill="none" stroke="#111" stroke-width="1.6"/>
        <rect x="3.5" y="3.5" width="31" height="11" rx="1.5" fill="#111"/>
        <rect x="38.5" y="6" width="2.5" height="6" rx="1" fill="#111"/>
      </svg>
    </div>
  </header>

  <h1 class="page-title">BADGES</h1>

  <div class="badge-track" aria-hidden="true"></div>

  <ul class="badge-list">
    <li class="badge" style="top:180px">
      <div class="badge-medal"><div class="badge-art art-bunny" role="img" aria-label="Bunny badge icon"></div></div>
      <p class="badge-text">2 point reduction for completing game in<br>under 35 minutes</p>
    </li>
    <li class="badge" style="top:325px">
      <div class="badge-medal"><div class="badge-art art-hat" role="img" aria-label="Hat badge icon"></div></div>
      <p class="badge-text">3 point reduction for sharing the app's selfie<br>pic to social media (can only be earned once )</p>
    </li>
    <li class="badge" style="top:469px">
      <div class="badge-medal"><div class="badge-art art-cat" role="img" aria-label="Cat badge icon"></div></div>
      <p class="badge-text">4 point reduction for taking zero clues</p>
    </li>
    <li class="badge" style="top:614px">
      <div class="badge-medal"><div class="badge-art art-mushroom" role="img" aria-label="Mushroom badge icon"></div></div>
      <p class="badge-text">2 point reduction for taking 1-2 clues entire<br>game</p>
    </li>
    <li class="badge" style="top:767px">
      <div class="badge-medal"><div class="badge-art art-cards" role="img" aria-label="Playing cards badge icon"></div></div>
      <p class="badge-text">2 point reduction for having par or less than<br>par score</p>
    </li>
    <li class="badge" style="top:912px">
      <div class="badge-medal"><div class="badge-art art-tart" role="img" aria-label="Tart badge icon"></div></div>
      <p class="badge-text">1 point reduction for having multiple hole<br>in ones</p>
    </li>
  </ul>

  <nav class="nav-actions">
    <button class="nav-button nav-back" type="button">BACK</button>
    <button class="nav-button nav-next" type="button">NEXT</button>
  </nav>
</main>
</body>
</html>
```